Webdesign für Stahl- und Brückenbauunternehmen
Zielgruppe
Wir haben 180 Jahre Erfahrung im Stahl- und Brückenbau.
Unsere Auftraggeber ist die öffentliche Hand.
Aufgabenstellung
Das ODLA / TKU-Logo soll mit rein (siehe jetzige Webseite)

```html
<!DOCTYPE html>
<html lang="de">
<head>
<meta charset="utf-8">
<title>KSW – Stahl- und Brückenbau</title>
<link href="https://fonts.googleapis.com/css2?family=Open+Sans:wght@400;600;700&display=swap" rel="stylesheet">
<style>
:root{
  --navy:#0b3f63;
  --navy-deep:#052a46;
  --gold:#e3a826;
  --blue:#3f97e8;
  --frame:#5aa5ee;
  --paper:#f8f8f8;
  --white:#ffffff;
  --ink:#1f2b36;
  --muted:#c7d4e0;
  --photo:#8f9a90;
}
*{margin:0;padding:0;box-sizing:border-box}
html,body{width:1200px;height:900px;overflow:hidden}
body{font-family:"Open Sans",sans-serif;background:var(--paper);position:relative}
.hero-bg{position:absolute;left:0;top:0;width:1200px;height:900px}
.brand{position:absolute;left:100px;top:30px;display:flex;align-items:center;gap:12px}
.brand-mark{width:36px;height:36px;background:var(--blue)}
.brand-text{display:flex;flex-direction:column}
.brand-name{color:var(--white);font-weight:700;font-size:36px;line-height:40px;letter-spacing:1px}
.brand-sub{color:var(--white);font-weight:600;font-size:9px;line-height:12px}
.nav{position:absolute;top:57px;left:380px;display:flex;gap:27px}
.nav a{color:var(--white);font-size:12.5px;font-weight:600;text-decoration:none}
.btn-contact{position:absolute;left:1026px;top:53px;width:73px;height:32px;background:var(--gold);color:var(--white);font-size:12.5px;font-weight:600;display:flex;align-items:center;justify-content:center}
.hero-title{position:absolute;left:101px;top:266px;color:var(--white);font-size:40px;font-weight:700;line-height:49px}
.hero-text{position:absolute;left:102px;top:375px;width:420px;color:var(--muted);font-size:15px;line-height:26px}
.btn-outline{position:absolute;left:105px;top:499px;width:152px;height:34px;border:2px solid var(--gold);color:var(--gold);font-size:13.5px;font-weight:600;display:flex;align-items:center;justify-content:center}
.link-projects{position:absolute;left:286px;top:507px;color:var(--gold);font-size:13.5px;font-weight:600}
.hero-visual{position:absolute;left:0;top:0;width:1200px;height:900px;pointer-events:none}
.intro-title{position:absolute;left:100px;top:878px;color:var(--ink);font-size:20px;font-weight:600;line-height:28.5px;width:320px}
.services{position:absolute;left:610px;top:810px;display:grid;grid-template-columns:repeat(3,163px);grid-auto-rows:163px}
.service{display:flex;flex-direction:column;align-items:center;padding-top:43px;gap:14px;font-size:12.5px;color:var(--ink)}
.service.is-white{background:var(--white)}
.service-icon{width:58px;height:58px;background:var(--blue);display:flex;align-items:center;justify-content:center}
.bracket{position:absolute;left:1100px;top:831px;width:17px;height:100px;border-top:3px solid var(--frame);border-right:3px solid var(--frame)}
</style>
</head>
<body>
<svg class="hero-bg" viewBox="0 0 1200 900" aria-hidden="true">
  <defs>
    <linearGradient id="heroGrad" x1="0" y1="0" x2="1" y2="1">
      <stop offset="0" stop-color="#0d4a73"/>
      <stop offset="1" stop-color="#04263f"/>
    </linearGradient>
  </defs>
  <path d="M0 0H1200V490L0 698Z" fill="url(#heroGrad)"/>
</svg>

<header>
  <div class="brand">
    <div class="brand-mark"></div>
    <div class="brand-text">
      <span class="brand-name">KSW</span>
      <span class="brand-sub">Kessler Stahlwerk GmbH</span>
    </div>
  </div>
  <nav class="nav">
    <a href="#">Home</a><a href="#">Unternehmen</a><a href="#">Leistungen</a><a href="#">Referenzen</a><a href="#">Stellenangebote</a>
  </nav>
  <div class="btn-contact">Kontakt</div>
</header>

<h1 class="hero-title">Ihr Spezialist für<br>anspruchsvolle Projekte</h1>
<p class="hero-text">Durch die 180-jährige traditionsreiche Vergangenheit und Erfahrung im Stahl- und Brückenbau geprägt, können wir auch zum Erfolg Ihres Projektes beitragen.</p>
<div class="btn-outline">Unsere Leistungen</div>
<div class="link-projects">Aktuelle Projekte</div>

<svg class="hero-visual" viewBox="0 0 1200 900">
  <polyline points="688,186 684,700 1090,670 1090,662" fill="none" stroke="var(--frame)" stroke-width="3"/>
  <path d="M691 179 L1095 204 L1095 667 L691 690Z" fill="var(--photo)" role="img" aria-label="Foto: Stahlfachwerkbrücke über einen Fluss"/>
</svg>

<h2 class="intro-title">Wir übernehmen Ihr anspruchsvolles Projekt von Anfang bis Ende.</h2>

<div class="services">
  <div class="service">
    <div class="service-icon"><svg width="30" height="30" viewBox="0 0 30 30"><rect x="5" y="3" width="20" height="24" fill="#fff"/><path d="M12 8h6l-1.5 6 2.5 4-4 5-4-5 2.5-4z" fill="var(--blue)"/></svg></div>
    <span>Projektionsplanung</span>
  </div>
  <div class="service is-white">
    <div class="service-icon"><svg width="30" height="30" viewBox="0 0 30 30"><path d="M12 6l8 0 4 4-6 6-3-3L8 24 5 21 12 14 9 11z" fill="#fff"/></svg></div>
    <span>Fertigung</span>
  </div>
  <div class="service">
    <div class="service-icon"><svg width="30" height="30" viewBox="0 0 30 30"><rect x="4" y="4" width="18" height="8" fill="#fff"/><path d="M22 8h4v8H15v4" fill="none" stroke="#fff" stroke-width="2.5"/><rect x="12" y="19" width="6" height="9" fill="#fff"/></svg></div>
    <span>Farbgebung &amp; FVZ</span>
  </div>
  <div class="service is-white">
    <div class="service-icon"><svg width="30" height="30" viewBox="0 0 30 30"><rect x="14" y="6" width="12" height="14" fill="#fff"/><rect x="4" y="14" width="12" height="7" fill="#fff"/><circle cx="9" cy="23" r="3" fill="#fff"/><circle cx="21" cy="23" r="3" fill="#fff"/></svg></div>
    <span>Transport</span>
  </div>
  <div class="service">
    <div class="service-icon"><svg width="30" height="30" viewBox="0 0 30 30"><path d="M24 5a6 6 0 0 0-7 8L5 25l2 2 12-12a6 6 0 0 0 8-7l-4 4-3-3z" fill="#fff"/></svg></div>
    <span>Montage</span>
  </div>
  <div class="service is-white">
    <div class="service-icon"><svg width="30" height="30" viewBox="0 0 30 30"><circle cx="11" cy="11" r="4" fill="#fff"/><path d="M9 20a5 5 0 0 1 4-8 6 6 0 0 1 11 2 3 3 0 0 1 0 6z" fill="#fff"/><path d="M11 23l-1 3M15 23l-1 3M19 23l-1 3" stroke="#fff" stroke-width="1.5"/></svg></div>
    <span>Korrosionsschutz</span>
  </div>
</div>
<div class="bracket"></div>
</body>
</html>
```